Refresh of graphic design for existing website

We would like to refresh our website. Please see the attached design specifications.

Industry/Entity Type

Graphic Design

```html
<!DOCTYPE html>
<html lang="en">
<head>
<meta charset="utf-8">
<title>VTA – The Vehicle Tooling Association</title>
<link href="https://fonts.googleapis.com/css2?family=Open+Sans:wght@400;600;700&family=Oswald:wght@300;400&display=swap" rel="stylesheet">
<style>
:root{
  --blue:#1b74c9;
  --blue-dark:#135a9e;
  --red:#d23a2e;
  --nav:#3b3e43;
  --band:#3e4147;
  --ink:#444a50;
  --muted:#80868c;
  --light:#ececec;
  --rule:#d4d4d4;
  --white:#ffffff;
}
*{box-sizing:border-box;margin:0;padding:0}
html,body{width:774px;height:1200px;overflow:hidden;background:var(--white)}
body{font-family:"Open Sans",Arial,sans-serif;color:var(--ink);position:relative}
.display{font-family:"Oswald","Arial Narrow",sans-serif;font-weight:300;text-transform:uppercase}

/* header */
.site-header{position:absolute;top:0;left:0;width:774px;height:80px}
.brand{position:absolute;left:24px;top:8px;color:var(--blue);font-weight:700}
.brand-mark{display:flex;align-items:center;gap:8px;font-size:40px;line-height:44px}
.brand-mark .dot{width:14px;height:14px;border-radius:50%;background:var(--blue)}
.brand-tag{font-size:11px;line-height:14px;margin-top:2px}
.social{position:absolute;left:462px;top:14px;display:flex;gap:10px}
.social span{width:14px;height:14px;background:#9aa0a6;border-radius:2px}
.login{position:absolute;left:556px;top:10px;width:200px;font-size:8px;color:var(--muted)}
.login .row{display:flex;gap:6px;align-items:center;margin-bottom:5px}
.login .field{flex:1;height:14px;border:1px solid var(--rule);padding:1px 4px;line-height:10px}
.login .btn{background:var(--nav);color:var(--white);padding:2px 6px;font-weight:700}
.login .check{width:8px;height:8px;border:1px solid var(--muted)}

/* nav */
.main-nav{position:absolute;top:80px;left:0;width:774px;height:22px;background:var(--nav);display:flex;padding-left:28px}
.main-nav a{color:var(--white);text-decoration:none;font-size:10px;line-height:22px;padding:0 13px}
.main-nav a.active{background:var(--blue)}

/* hero */
.hero{position:absolute;top:102px;left:0;width:774px;height:306px;
  background:linear-gradient(100deg,#2f4a66 0%,#587894 35%,#7f97ab 60%,#4a5d70 100%)}
.hero-title{position:absolute;left:90px;top:118px;color:var(--white);font-size:26px;line-height:32px;letter-spacing:1px}
.search{position:absolute;left:90px;top:196px;width:240px;height:32px;background:var(--blue);display:flex;align-items:center;padding-left:12px;color:var(--white);font-size:11px}
.search svg{position:absolute;right:8px;top:8px}

/* welcome */
.welcome{position:absolute;top:408px;left:0;width:774px;height:240px;text-align:center;padding:30px 50px 0}
.welcome h1{color:var(--blue);font-size:28px;letter-spacing:1px;margin-bottom:24px}
.welcome p{font-size:10.5px;line-height:17px;color:var(--muted);margin-bottom:16px}

/* member band */
.member-band{position:absolute;top:650px;left:0;width:774px;height:124px;background:var(--band)}
.member-band svg.join-shape{position:absolute;left:0;top:0}
.join-label{position:absolute;left:60px;top:52px;color:var(--white);font-size:20px}
.band-text{position:absolute;left:318px;top:38px;color:var(--white)}
.band-text h2{font-size:24px;letter-spacing:1px}
.band-text p{font-size:11px;margin-top:2px}
.band-text strong{color:#5aa6ee}
.band-btn{position:absolute;left:586px;top:50px;width:82px;height:22px;background:#55595f;color:var(--white);font-size:10px;text-align:center;line-height:22px;font-weight:600}

/* events and blog */
.feeds{position:absolute;top:784px;left:0;width:774px;height:216px}
.feed{position:absolute;top:0;width:356px}
.feed.events{left:22px}.feed.blog{left:398px}
.feed-head{display:flex;justify-content:space-between;align-items:flex-end;border-bottom:1px solid var(--rule);padding-bottom:4px;margin-bottom:12px}
.feed-head h3{color:var(--blue);font-size:20px}
.arrows{display:flex;gap:3px}
.arrows span{width:16px;height:14px;background:#9aa0a6;display:flex;align-items:center;justify-content:center}
.card{display:flex;gap:12px}
.thumb{width:128px;height:150px;flex:none;background:linear-gradient(135deg,#8aa0b3,#c8ccd0 55%,#5c6e80)}
.card h4{font-size:11px;font-weight:700;color:var(--ink)}
.card .date{font-size:9px;color:var(--red);margin:3px 0 8px}
.card p{font-size:9px;line-height:13px;color:var(--muted)}
.card .more{display:inline-block;margin-top:12px;background:var(--blue);color:var(--white);font-size:9px;font-weight:700;padding:4px 12px}

/* footer */
.site-footer{position:absolute;top:1004px;left:0;width:774px;height:174px;background:var(--light);padding:16px 22px}
.footer-links{position:absolute;top:18px;font-size:8px;line-height:14px;color:var(--muted);list-style:none}
.footer-links li::before{content:"› ";color:var(--blue)}
.col1{left:26px}.col2{left:180px}.col3{left:334px;width:170px}
.news{position:absolute;left:540px;top:14px;width:212px}
.news h3{color:var(--blue);font-size:18px;margin-bottom:8px}
.news li{list-style:none;font-size:8px;line-height:11px;color:var(--muted);margin-bottom:8px}
.news .d{color:var(--red);display:block}
.copyright{position:absolute;top:1178px;left:0;width:774px;height:22px;background:var(--nav);color:#b9bdc1;font-size:8px;text-align:center;line-height:22px}
</style>
</head>
<body>

<header class="site-header">
  <div class="brand">
    <div class="brand-mark">VTA <span class="dot"></span></div>
    <div class="brand-tag">The Vehicle Tooling Association</div>
  </div>
  <div class="social" aria-label="Social links"><span></span><span></span><span></span></div>
  <form class="login">
    <div class="row"><span class="field">Email</span><span class="field">Password</span></div>
    <div class="row"><span>Forgot password</span><span class="check"></span><span>Remember me</span><span class="btn">LOGIN</span></div>
  </form>
</header>

<nav class="main-nav">
  <a class="active" href="#">Home</a><a href="#">About Us</a><a href="#">Membership</a><a href="#">VTA Members</a><a href="#">VTA Events</a><a href="#">TechShelf Library</a><a href="#">Market Research</a><a href="#">Hidden Files</a>
</nav>

<section class="hero" role="img" aria-label="Photo of a mechanic in blue overalls holding a wheel wrench in a workshop">
  <h1 class="hero-title display">Advancing the vehicle service<br>industry since 1947</h1>
  <div class="search">Enter search string
    <svg width="16" height="16" viewBox="0 0 16 16"><circle cx="6.5" cy="6.5" r="5" fill="none" stroke="#fff" stroke-width="2"/><line x1="10" y1="10" x2="15" y2="15" stroke="#fff" stroke-width="2"/></svg>
  </div>
</section>

<section class="welcome">
  <h1 class="display">Welcome to our site</h1>
  <p>VTA's Mission is to advance the vehicle service industry by providing technical data and open dialog between the manufacturers of transportation products, government regulators and the providers of tools, equipment and service information.</p>
  <p>VTA is one of the most respected trade associations in the automotive aftermarket, giving fair and equitable representation to all segments of the equipment and tool industry. The Association is an association of automotive tool and equipment manufacturers and technical information providers and training organizations.</p>
</section>

<section class="member-band">
  <svg class="join-shape" width="250" height="124" viewBox="0 0 250 124"><polygon points="0,0 200,0 250,62 200,124 0,124" fill="#1b74c9"/><circle cx="40" cy="62" r="10" fill="#fff"/></svg>
  <div class="join-label display">Join VTA</div>
  <div class="band-text">
    <h2 class="display">Member benefits</h2>
    <p>with special Auto service <strong>Discount</strong> and <strong>Benefits</strong></p>
  </div>
  <div class="band-btn">CLICK HERE</div>
</section>

<section class="feeds">
  <div class="feed events">
    <div class="feed-head"><h3 class="display">Upcoming events</h3>
      <div class="arrows"><span><svg width="6" height="8"><polygon points="6,0 0,4 6,8" fill="#fff"/></svg></span><span><svg width="6" height="8"><polygon points="0,0 6,4 0,8" fill="#fff"/></svg></span></div></div>
    <div class="card">
      <div class="thumb" role="img" aria-label="Photo of a technician at work on a vehicle"></div>
      <div><h4>PartsLine Show</h4><div class="date">19 Dec 2013</div>
        <p>Join us at the annual trade expo for new tools, hands-on demos and member talks.</p>
        <span class="more">CLICK HERE</span></div>
    </div>
  </div>
  <div class="feed blog">
    <div class="feed-head"><h3 class="display">VTA news blog</h3>
      <div class="arrows"><span><svg width="6" height="8"><polygon points="6,0 0,4 6,8" fill="#fff"/></svg></span><span><svg width="6" height="8"><polygon points="0,0 6,4 0,8" fill="#fff"/></svg></span></div></div>
    <div class="card">
      <div class="thumb" role="img" aria-label="Photo of a mechanic checking an engine bay"></div>
      <div><h4>Inside the Modern Diagnostic Console</h4><div class="date">19 Dec 2013</div>
        <p>Our members look at how shop consoles read vehicle data today, what changed in the last year and how service teams can stay ready for the next wave of tools.</p>
        <span class="more">CLICK HERE</span></div>
    </div>
  </div>
</section>

<footer class="site-footer">
  <ul class="footer-links col1"><li>Industry Groups</li><li>Member Events</li><li>Member Companies</li><li>Active Participants</li><li>Annual Meeting Guide</li><li>Market Research Survey</li><li>Payment Center</li></ul>
  <ul class="footer-links col2"><li>Staff Directory Tool Update</li><li>Benchmark Report</li><li>Event Log</li><li>Online Exhibition</li><li>Videos and Newsletter</li><li>Guidelines</li></ul>
  <ul class="footer-links col3"><li>Contact Us</li><li>Click here to view the innovation guide</li><li>Further details on member application</li><li>See the technician quick guide</li><li>Click to view</li></ul>
  <div class="news">
    <h3 class="display">Industry news</h3>
    <ul>
      <li><span class="d">15 Dec 2013</span>New members join the annual tooling meeting</li>
      <li><span class="d">12 Dec 2013</span>Shop data standards update now available online</li>
      <li><span class="d">08 Dec 2013</span>Survey results show steady growth for service equipment</li>
    </ul>
  </div>
</footer>
<div class="copyright">Copyright © 2014 VTA The Vehicle Tooling Association</div>

</body>
</html>
```